7:40 Steady Compass- A Handbook For Shaping Your Daily Conduct Each Morning

7:40 Steady Compass
A Handbook For Shaping Your Daily Conduct Each Morning

It will be a 6 X 9 guide that is meant for people to keep with them with pages to fill out. See supporting pics for overall pillars that are discussed and form basis of the solution.

I will need a spine and back cover as well.

My blog and content: www.morvenqlisk.com

Target Market(s)

Business professionals, senior emergency services people

Industry/Entity Type

Business Management

Font styles to use
Serif

Colors

Designer to choose colors to be used in the design.

Requirements
Must have
• Clean look, easily recognizable among other books. Front cover and back and spine. My picture on the back somewhere (corner maybe?!)
Nice to have
• Easily recognizeable
• NOTE: Graphic should read Today, Was I the Leader That I Would Want? I uploaded graphic that says ..."I Would've Wanted" which is incorrect.
Should not have
• Busy cover

```html
<!DOCTYPE html>
<html lang="en">
<head>
<meta charset="utf-8">
<title>7:40 Steady Compass – Book Cover</title>
<link href="https://fonts.googleapis.com/css2?family=Oswald:wght@700&family=Questrial&family=Jost:wght@400;500;700&family=Arimo:wght@400;700&family=Mrs+Saint+Delafield&display=swap" rel="stylesheet">
<style>
  :root {
    --backdrop: #222121;
    --navy: #03045a;
    --red: #ec3237;
    --red-line: #d92a2f;
    --yellow: #fff200;
    --white: #ffffff;
    --ink: #2b2b2b;
  }
  * { margin: 0; padding: 0; box-sizing: border-box; }
  html, body { width: 1200px; height: 996px; overflow: hidden; background: var(--backdrop); }
  .canvas { position: relative; width: 1200px; height: 996px; }

  .panel { position: absolute; top: 88px; height: 759px; overflow: hidden; }
  .back-cover { left: 38px; width: 517px; }
  .spine { left: 555px; width: 75px; background: var(--navy); }
  .front-cover { left: 630px; width: 501px; }

  .band-top { position: absolute; left: 0; top: 0; width: 100%; height: 444px; background: var(--navy); }
  .band-bottom { position: absolute; left: 0; top: 444px; width: 100%; height: 315px; background: var(--red); }

  /* Back cover */
  .back-heading { position: absolute; left: 54px; top: 68px; font-family: 'Jost', sans-serif; font-weight: 700; font-size: 16px; color: var(--white); letter-spacing: 0.2px; }
  .crisis-label { position: absolute; left: 54px; top: 122px; font-family: 'Jost', sans-serif; font-weight: 700; font-size: 17px; color: var(--white); }
  .steps { position: absolute; left: 54px; top: 158px; font-family: 'Arimo', sans-serif; font-size: 18px; line-height: 24px; color: var(--white); list-style: none; }
  .steps li { margin-bottom: 22px; }
  .steps .prompt { color: var(--yellow); font-weight: 700; display: block; }
  .steps .prompt.indent { padding-left: 5px; }
  .steps .inline-prompt { color: var(--yellow); font-weight: 700; }

  .author-photo { position: absolute; left: 44px; top: 455px; width: 200px; height: 195px; background: linear-gradient(160deg, #5a5a5a 0%, #2e2e2e 55%, #1c1c1c 100%); }
  .about-box { position: absolute; left: 253px; top: 455px; width: 236px; height: 195px; border: 1px solid var(--red-line); display: flex; align-items: center; justify-content: center; padding-bottom: 40px; font-family: 'Arimo', sans-serif; font-size: 22px; color: var(--ink); }
  .back-url { position: absolute; left: 0; width: 100%; top: 720px; text-align: center; font-family: 'Questrial', sans-serif; font-size: 15px; color: var(--white); letter-spacing: 0.3px; }

  /* Spine */
  .spine-title { position: absolute; left: 17px; top: 701px; transform: rotate(-90deg); transform-origin: 0 0; white-space: nowrap; font-family: 'Questrial', sans-serif; font-size: 40px; line-height: 1; color: var(--white); }
  .spine-title .num { color: var(--yellow); }
  .spine-author { position: absolute; left: -28px; top: 67px; width: 130px; height: 40px; transform: rotate(-90deg); transform-origin: 50% 50%; white-space: nowrap; text-align: center; font-family: 'Mrs Saint Delafield', cursive; font-size: 26px; line-height: 40px; color: var(--white); }

  /* Front cover */
  .tagline { position: absolute; left: 0; width: 100%; top: 29px; text-align: center; font-family: 'Jost', sans-serif; font-weight: 700; font-size: 13.5px; color: var(--white); letter-spacing: 0.2px; }
  .title-number { position: absolute; left: 70px; top: 85px; font-family: 'Oswald', sans-serif; font-weight: 700; font-size: 185px; line-height: 1; color: var(--yellow); letter-spacing: -3px; }
  .title-words { position: absolute; left: 73px; top: 280px; font-family: 'Questrial', sans-serif; font-size: 48px; line-height: 42px; color: var(--white); }

  .pillars-head { position: absolute; left: 72px; top: 466px; display: flex; align-items: flex-start; }
  .pillars-count { font-family: 'Jost', sans-serif; font-weight: 400; font-size: 52px; line-height: 44px; color: var(--yellow); margin-right: 2px; }
  .pillars-lines { font-family: 'Jost', sans-serif; font-size: 21px; line-height: 23px; color: var(--white); padding-top: 2px; }
  .pillars-lines strong { font-weight: 700; display: block; }
  .pillars-list { position: absolute; left: 72px; top: 530px; font-family: 'Jost', sans-serif; font-weight: 500; font-variant: small-caps; font-size: 16px; line-height: 22px; color: var(--navy); }
  .pillars-list .dot { color: var(--white); margin-right: 5px; }
  .pillars-list span + .dot { margin-left: 5px; }

  .front-author { position: absolute; left: 0; width: 100%; top: 688px; text-align: center; font-family: 'Mrs Saint Delafield', cursive; font-size: 38px; line-height: 1; color: var(--white); padding-right: 40px; }
</style>
</head>
<body>
<div class="canvas">

  <section class="panel back-cover">
    <div class="band-top"></div>
    <div class="band-bottom"></div>
    <h2 class="back-heading">HOW TO BE THE LEADER YOU WOULD WANT</h2>
    <p class="crisis-label">During crisis:</p>
    <ol class="steps">
      <li>1. Daily ,Ask yourself:<span class="prompt indent">“Today, was I the leader I would want ?”</span></li>
      <li>2.if the answer is no<span class="prompt">“How can I improve?”</span></li>
      <li>3. <span class="inline-prompt">Improve</span><br>1%each day is a big deal.</li>
    </ol>
    <div class="author-photo" role="img" aria-label="Black and white portrait photo of the author"></div>
    <div class="about-box">About You</div>
    <p class="back-url">www.morvenqlisk.com</p>
  </section>

  <section class="panel spine">
    <p class="spine-author">Morven Q. Lisk</p>
    <p class="spine-title"><span class="num">7:40</span> Steady Compass</p>
  </section>

  <section class="panel front-cover">
    <div class="band-top"></div>
    <div class="band-bottom"></div>
    <p class="tagline">A HANDBOOK FOR SHAPING YOUR DAILY CONDUCT EACH MORNING</p>
    <h1 class="title-number">7:40</h1>
    <p class="title-words">Steady<br>Compass</p>
    <div class="pillars-head">
      <span class="pillars-count">4</span>
      <p class="pillars-lines">Personal Pillars Of<strong>Effective Leadership</strong></p>
    </div>
    <p class="pillars-list">
      <span class="dot">•</span>Vulnerability<span class="dot">•</span>Compassion<br>
      <span class="dot">•</span>Empathy <span class="dot">•</span>Personal Stress Management
    </p>
    <p class="front-author">Morven Q. Lisk</p>
  </section>

</div>
</body>
</html>
```